Agricultural equipment sales and financing flyer

I need an agricultural sales and financing flyer that can double as a contact poster that you would put on a bulletin board with contact information and phone number in the form of tear off stubs ast the bottom and contact info on the main poster. For efficiencies sake, I want this poster/flyer to be dimensioned to fit on 8.5x11 inch sheet of paper.

I've included a logo for our company for you to use in the creation of this poster. When making the poster, follow the color scheme on the logo (orange, black and a little bit of red) this is our brand coloring.

-I do not want a poster that looks like it was made with scrap art images in microsoft word
-I've included a very rough sketch of what I envisioned in a poster, my designing clearly sucks in hindsight, but follow what the format looks like (ei logo near the top, target market below it, then services offered, then why our services are better and at the bottom, removable cut away tickets of phone contact information.
-I want the ability to change the worded content so that if our address or phone number or any details change, I can simply open this file, for example, in Microsoft Publisher and just input new details and reprint.

Target Market(s)

farmers

Industry/Entity Type

Agriculture

Font styles to use
Other font styles liked:
• Just use a professional looking, simple font

Colors
f78f20
ec1f27
000000
606060
ffffff
f5f5f5
eaeaea

Requirements
Must have
• -8.5x11 inch dimensioned poster
• -use company colors as sampled in logo attached
• -removable contact information tabs at bottom of poster that people can remove from poster
Nice to have
• -although i have listed general colors used below. Only use colors a sampled from the logo.
Should not have
• -a dark background, i don't want to pay a fortune in ink costs at the printer

```html
<!DOCTYPE html>
<html lang="en">
<head>
<meta charset="utf-8">
<title>Agricultural Solutions Flyer</title>
<link rel="stylesheet" href="https://fonts.googleapis.com/css2?family=Mulish:wght@700;800&family=Arimo:ital,wght@0,400;0,700;1,700&display=swap">
<style>
  :root {
    --orange: #f78f20;
    --red: #ec1f27;
    --black: #000000;
    --grey: #606060;
    --white: #ffffff;
    --band-soft: #fde3e3;
    --band-mid: #f8b4b4;
    --band-strong: #f48a8a;
  }
  * { margin: 0; padding: 0; box-sizing: border-box; }
  html, body { width: 927px; height: 1200px; overflow: hidden; background: var(--white); }
  .flyer {
    position: relative;
    width: 927px;
    height: 1200px;
    background: var(--white);
    overflow: hidden;
    font-family: "Mulish", sans-serif;
  }
  .backdrop { position: absolute; inset: 0; }

  .brand-mark {
    position: absolute;
    left: 0; right: 0; top: 40px;
    display: flex; flex-direction: column; align-items: center; gap: 10px;
  }
  .brand-mark__dot {
    width: 150px; height: 150px; border-radius: 50%;
    background: var(--black);
  }
  .brand-mark__name {
    font-family: "Mulish", sans-serif;
    font-weight: 800; font-size: 20px; color: var(--orange);
  }

  .solutions { position: absolute; left: 88px; top: 268px; width: 780px; }
  .solutions__title {
    font-weight: 800; font-size: 46px; color: var(--red);
    margin-left: 27px; margin-bottom: 8px; letter-spacing: -0.3px;
  }
  .solutions__list { list-style: none; }
  .solutions__item {
    position: relative; padding-left: 26px;
    font-weight: 700; font-size: 29px; line-height: 33px; color: var(--red);
  }
  .solutions__item::before {
    content: ""; position: absolute; left: 2px; top: 10px;
    width: 18px; height: 12px; border-radius: 50%; background: var(--black);
  }
  .solutions__item + .solutions__item { margin-top: 2px; }
  .solutions__tagline { display: block; color: var(--black); }

  .benefits { position: absolute; left: 112px; top: 612px; width: 700px; }
  .benefits__title {
    font-weight: 700; font-size: 34px; color: var(--orange);
    text-decoration: underline; text-decoration-thickness: 2px; text-underline-offset: 5px;
    margin-bottom: 10px;
  }
  .benefits__list { list-style: none; font-family: "Arimo", sans-serif; font-size: 23.5px; line-height: 32px; color: var(--orange); }
  .benefits__list li .dash { color: var(--grey); }
  .benefits__indent { padding-left: 16px; }

  .contact-block {
    position: absolute; left: 583px; top: 878px; width: 300px; text-align: left;
  }
  .contact-block__name {
    font-weight: 800; font-size: 23px; color: var(--orange); line-height: 1.15;
  }
  .contact-block__trade {
    font-family: "Arimo", sans-serif; font-style: italic; font-weight: 700;
    font-size: 13px; color: var(--red); margin: 4px 0 0 22px;
  }
  .contact-block__phone {
    font-family: "Arimo", sans-serif; font-weight: 700; font-size: 30px;
    color: var(--red); letter-spacing: 2px; margin: 4px 0 0 14px;
  }

  .tear-strip { position: absolute; left: 0; top: 984px; width: 927px; height: 216px; }
</style>
</head>
<body>
<main class="flyer">
  <svg class="backdrop" width="927" height="1200" viewBox="0 0 927 1200" aria-hidden="true">
    <polygon points="210,0 927,0 927,140 700,108 420,40" fill="var(--band-mid)"/>
    <polygon points="330,0 927,0 927,70 640,50" fill="var(--band-strong)" opacity="0.55"/>
    <polygon points="0,1060 0,1200 150,1200 927,690 927,560" fill="var(--band-soft)"/>
    <polygon points="927,560 927,712 610,905 560,870" fill="var(--band-mid)" opacity="0.8"/>
  </svg>

  <header class="brand-mark">
    <span class="brand-mark__dot"></span>
    <span class="brand-mark__name">Ridgeline Production Services Ltd.</span>
  </header>

  <section class="solutions">
    <h1 class="solutions__title">Agricultural Solutions</h1>
    <ul class="solutions__list">
      <li class="solutions__item">Felxible leasing and financing options that will turn heads and keep costs down</li>
      <li class="solutions__item">24 hour maintenance services for your machines
        <span class="solutions__tagline">Let no breakdowns leave you in the dust</span></li>
    </ul>
  </section>

  <section class="benefits">
    <h2 class="benefits__title">Benefits Offered through us</h2>
    <ul class="benefits__list">
      <li><span class="dash">-</span> Alberta based solutions that keep you high and dry</li>
      <li><span class="dash">-</span> Commercial wholesale rates on leasing and financing</li>
      <li><span class="dash">-</span> Long term relationships, personal relationships: Myself</li>
      <li><span class="dash">-</span> Promt customer service delivered Alberta location</li>
      <li class="benefits__indent">(in part by veterans)</li>
    </ul>
  </section>

  <aside class="contact-block">
    <div class="contact-block__name">RIDGELINE<br>Production Services Ltd.</div>
    <div class="contact-block__trade">Oilfield Services &amp; Maintenance</div>
    <div class="contact-block__phone">780-555-0142</div>
  </aside>

  <svg class="tear-strip" width="927" height="216" viewBox="0 0 927 216" aria-label="Tear-off contact tabs">
    <g stroke="var(--black)" stroke-width="2" stroke-dasharray="12 8" fill="none">
      <line x1="0" y1="14" x2="866" y2="14"/>
      <line x1="114" y1="14" x2="114" y2="216"/>
      <line x1="250" y1="14" x2="250" y2="216"/>
      <line x1="397" y1="14" x2="397" y2="216"/>
      <line x1="538" y1="14" x2="538" y2="216"/>
      <line x1="670" y1="14" x2="670" y2="216"/>
      <line x1="803" y1="14" x2="803" y2="216"/>
    </g>
    <g class="scissors" stroke="var(--black)" stroke-width="2.5" fill="none">
      <circle cx="900" cy="5" r="5.5"/>
      <circle cx="900" cy="23" r="5.5"/>
      <line x1="896" y1="9" x2="872" y2="22"/>
      <line x1="896" y1="19" x2="872" y2="6"/>
    </g>
  </svg>
</main>
</body>
</html>
```